Corvane semiconductor corporate presentation

We need a new template with some fresh design elements as we've just announced the acquisition of a new company. Similarly, the backend of the ppt is not set up correctly - and doesn't format properly when dropping in copied text. Attached is the powerpoint presentation/ template as it stands today.
Industry/Entity Type
It Company
Font styles to use
Other font styles liked:
- Arial
Look and feel
Each slider illustrates characteristics of the customer's brand and the style your logo design should communicate.

```html
<!DOCTYPE html>
<html lang="en">
<head>
<meta charset="utf-8">
<title>Corvane semiconductor – presentation template</title>
<link rel="stylesheet" href="https://fonts.googleapis.com/css2?family=Raleway:wght@300;400;600;700&family=Open+Sans:wght@400;600;700&display=swap">
<style>
:root{
  --teal:#16a0bd;
  --cyan:#29b6d8;
  --sky:#5cc6e4;
  --green:#8dc63f;
  --purple:#8b2a8d;
  --magenta:#e4097e;
  --orange:#f7941d;
  --ink:#4a4a4a;
  --mute:#9c9c9c;
  --line:#e2e2e2;
  --paper:#ffffff;
  --canvas:#ffffff;
}
*{box-sizing:border-box;margin:0;padding:0}
html,body{width:1200px;height:3775px;overflow:hidden;background:var(--canvas)}
body{font-family:"Open Sans",Arial,sans-serif;color:var(--ink)}
.deck{width:1200px;height:3775px;padding:13px 6px 14px;display:grid;grid-template-columns:repeat(3,390px);grid-template-rows:repeat(13,280px);gap:9px}
.slide{position:relative;overflow:hidden;background:var(--paper);box-shadow:0 0 0 1px #ececec}
.abs{position:absolute}
.slide-title{position:absolute;left:12px;top:9px;font-family:"Raleway",Arial,sans-serif;font-weight:400;font-size:15px;color:var(--teal)}
.foot{position:absolute;left:10px;right:10px;bottom:7px;height:12px;display:flex;align-items:center;justify-content:space-between}
.foot .dot{width:10px;height:10px;border-radius:50%;background:var(--teal)}
.foot .legal{flex:1;text-align:right;padding-right:8px;font-size:5px;color:var(--mute)}
.foot .sq{width:9px;height:9px;background:var(--green)}
.ph{position:absolute}
.p{font-size:6px;line-height:1.5;color:var(--mute)}
.p-white{font-size:6px;line-height:1.5;color:rgba(255,255,255,.9)}
.h-small{font-family:"Raleway",Arial,sans-serif;font-weight:600;font-size:8px;color:var(--teal)}
.brand{display:inline-flex;align-items:center;gap:5px;font-family:"Raleway",Arial,sans-serif;font-weight:700;color:var(--teal)}
.brand i{display:inline-block;border-radius:50%;background:currentColor}
.brand i.sq{border-radius:0}
.brand-white{color:#fff}
.brand-green{color:#3fa34d}
.sep{display:inline-block;width:1px;background:#bbb}
.cover-title{font-family:"Raleway",Arial,sans-serif;font-weight:700;font-size:21px;letter-spacing:.2px}
.cover-sub{font-size:6px;margin-top:3px}
.section{color:#fff}
.section .ring{position:absolute;right:-50px;top:30px;width:260px;height:260px;border-radius:50%;background:rgba(255,255,255,.13)}
.section .mark{position:absolute;width:22px;height:22px;border:2px solid #fff;transform:rotate(45deg)}
.section .label{position:absolute;font-family:"Raleway",Arial,sans-serif;font-weight:600;font-size:14px}
.section .sub{position:absolute;width:160px;font-size:5.5px;line-height:1.5;color:rgba(255,255,255,.85)}
.circle{border-radius:50%}
.table{border-collapse:collapse;width:100%;font-size:5.5px;color:var(--ink)}
.table th{background:var(--teal);color:#fff;font-weight:600;padding:4px 3px;text-align:left}
.table td{padding:4px 3px;border-bottom:1px solid var(--line)}
.table tr:nth-child(even) td{background:#f3f9fb}
.num{font-family:"Raleway",Arial,sans-serif;font-weight:700}
</style>
</head>
<body>
<main class="deck">

<section class="slide cover">
  <div class="ph" role="img" aria-label="Photo of a hand holding a phone at a brightly lit concert" style="inset:0;background:linear-gradient(135deg,#0f3e58 0%,#1d8fae 45%,#6e4a9a 80%,#c4477c 100%)"></div>
  <div class="abs" style="left:14px;top:12px"><span class="brand brand-white" style="font-size:13px"><i style="width:10px;height:10px"></i>Corvane</span></div>
  <div class="abs" style="left:14px;top:190px;color:#fff">
    <div class="cover-title">YOUR TITLE GOES HERE</div>
    <div class="cover-sub">Your Subtitle Goes Here</div>
  </div>
</section>

<section class="slide cover">
  <div class="ph" role="img" aria-label="Photo of a smiling man working at a laptop in a bright office" style="inset:0;background:linear-gradient(90deg,#f4f5f6 0%,#e6e8ea 45%,#b9bfc5 75%,#8e969e 100%)"></div>
  <div class="abs" style="left:16px;top:14px;display:flex;align-items:center;gap:7px">
    <span class="brand" style="font-size:13px"><i style="width:10px;height:10px"></i>Corvane</span>
    <span class="sep" style="height:14px"></span>
    <span class="brand brand-green" style="font-size:10px"><i class="sq" style="width:9px;height:9px"></i>Pelleron</span>
  </div>
  <div class="abs" style="left:16px;top:188px;color:var(--teal)">
    <div class="cover-title">YOUR TITLE GOES HERE</div>
    <div class="cover-sub" style="color:var(--mute)">Your Subtitle Goes Here</div>
  </div>
</section>

<section class="slide cover">
  <svg class="abs" style="left:0;top:98px" width="240" height="20" viewBox="0 0 240 20"><polygon points="0,0 240,0 228,20 0,20" fill="var(--purple)"/></svg>
  <div class="abs" style="right:16px;top:98px;display:flex;align-items:center;gap:7px">
    <span class="brand" style="font-size:13px"><i style="width:10px;height:10px"></i>Corvane</span>
    <span class="sep" style="height:14px"></span>
    <span class="brand brand-green" style="font-size:10px"><i class="sq" style="width:9px;height:9px"></i>Pelleron</span>
  </div>
  <div class="abs" style="right:16px;top:134px;text-align:right">
    <div style="font-family:Raleway,Arial,sans-serif;font-weight:600;font-size:14px;color:var(--teal)">Your Title Goes Here</div>
    <div class="cover-sub" style="color:var(--mute)">Your Subtitle Goes Here</div>
  </div>
</section>

<section class="slide cover">
  <div class="abs" style="left:0;right:0;top:100px;display:flex;justify-content:center;align-items:center;gap:14px">
    <span class="brand" style="font-size:22px"><i style="width:17px;height:17px"></i>Corvane</span>
    <span class="sep" style="height:26px"></span>
    <span class="brand brand-green" style="font-size:16px"><i class="sq" style="width:15px;height:15px"></i>Pelleron</span>
  </div>
  <div class="abs" style="left:0;right:0;top:172px;text-align:center">
    <div style="font-family:Raleway,Arial,sans-serif;font-weight:600;font-size:16px;color:var(--teal)">Your Title Goes Here</div>
    <div class="cover-sub" style="color:var(--mute)">Your Subtitle Goes Here</div>
  </div>
  <div class="abs" style="left:0;right:0;top:220px;height:2px;background:var(--purple)"></div>
</section>

<section class="slide cover">
  <div class="ph" role="img" aria-label="Photo of a circuit board close-up" style="inset:0;background:linear-gradient(135deg,#c9d7dc,#7c9aa6)"></div>
  <svg class="abs" style="inset:0" width="390" height="280" viewBox="0 0 390 280"><polygon points="0,120 390,0 390,280 0,280" fill="var(--teal)" opacity=".95"/><polygon points="0,110 160,60 170,70 0,122" fill="var(--green)"/></svg>
  <div class="abs" style="left:14px;top:12px"><span class="brand" style="font-size:8px;color:#2e4a55"><i style="width:7px;height:7px"></i>Corvane</span></div>
  <div class="abs" style="left:36px;top:158px;color:#fff">
    <div style="font-family:Raleway,Arial,sans-serif;font-weight:700;font-size:17px">YOUR TITLE GOES HERE</div>
    <div class="cover-sub">Your Subtitle Goes Here</div>
  </div>
</section>

<section class="slide">
  <h2 class="slide-title">Our Agenda</h2>
  <div class="abs" style="left:70px;top:50px;width:300px;display:grid;grid-template-columns:1fr 1fr;row-gap:22px;column-gap:20px">
    <div style="display:flex;gap:6px"><span class="circle" style="width:16px;height:16px;border:2px solid var(--teal);flex:none"></span><div><div class="h-small">Agenda One</div><div class="p">Short note on this point.</div></div></div>
    <div style="display:flex;gap:6px"><span class="circle" style="width:16px;height:16px;border:2px solid var(--teal);flex:none"></span><div><div class="h-small">Agenda Four</div><div class="p">Short note on this point.</div></div></div>
    <div style="display:flex;gap:6px"><span class="circle" style="width:16px;height:16px;border:2px solid var(--teal);flex:none"></span><div><div class="h-small">Agenda Two</div><div class="p">Short note on this point.</div></div></div>
    <div style="display:flex;gap:6px"><span class="circle" style="width:16px;height:16px;border:2px solid var(--teal);flex:none"></span><div><div class="h-small">Agenda Five</div><div class="p">Short note on this point.</div></div></div>
    <div style="display:flex;gap:6px"><span class="circle" style="width:16px;height:16px;border:2px solid var(--teal);flex:none"></span><div><div class="h-small">Agenda Three</div><div class="p">Short note on this point.</div></div></div>
    <div style="display:flex;gap:6px"><span class="circle" style="width:16px;height:16px;border:2px solid var(--teal);flex:none"></span><div><div class="h-small">Agenda Six</div><div class="p">Short note on this point.</div></div></div>
  </div>
  <div class="foot"><span class="dot"></span><span class="legal">© 2024 Corvane Semiconductor · corvane-semi.example</span><span class="sq"></span></div>
</section>

<section class="slide">
  <h2 class="slide-title">Title And Image + Text</h2>
  <div class="ph" role="img" aria-label="Portrait photo of a businessman" style="left:12px;top:34px;width:172px;height:70px;background:linear-gradient(90deg,#e8edf0,#b6c2ca)"></div>
  <div class="abs" style="left:194px;top:34px;width:184px;height:70px;background:var(--cyan);display:flex;align-items:center;justify-content:center"><span class="brand brand-white" style="font-size:18px"><i style="width:14px;height:14px"></i>Corvane</span></div>
  <div class="abs" style="left:12px;top:114px;width:166px;font-family:Raleway,Arial,sans-serif;font-size:8px;line-height:1.5;color:var(--teal)">Short lead statement about this topic sits here in the brand colour for emphasis and clear reading.</div>
  <div class="abs p" style="left:194px;top:114px;width:184px">Short supporting text about this topic goes in this area. Short supporting text about this topic goes in this area. Short supporting text about this topic goes in this area.</div>
  <div class="foot"><span class="dot"></span><span class="legal">© 2024 Corvane Semiconductor · corvane-semi.example</span><span class="sq"></span></div>
</section>

<section class="slide">
  <h2 class="slide-title">Icon Slide</h2>
  <div class="abs" style="left:14px;top:40px;width:150px;display:flex;flex-direction:column;gap:22px">
    <div style="display:flex;gap:7px;align-items:center"><span class="circle" style="width:22px;height:22px;background:var(--teal);flex:none"></span><div><div class="h-small">Heading</div><div class="p">Short note on this point.</div></div></div>
    <div style="display:flex;gap:7px;align-items:center"><span class="circle" style="width:22px;height:22px;background:var(--teal);flex:none"></span><div><div class="h-small">Heading</div><div class="p">Short note on this point.</div></div></div>
    <div style="display:flex;gap:7px;align-items:center"><span class="circle" style="width:22px;height:22px;background:var(--teal);flex:none"></span><div><div class="h-small">Heading</div><div class="p">Short note on this point.</div></div></div>
  </div>
  <div class="ph" role="img" aria-label="Photo of a businessman in an office, tinted blue" style="left:184px;top:0;width:206px;height:258px;background:linear-gradient(160deg,#5fb8d4,#1d7f9e)"></div>
  <div class="abs" style="left:196px;top:40px;display:flex;flex-direction:column;gap:22px">
    <div style="display:flex;gap:7px;align-items:center"><span class="circle" style="width:22px;height:22px;background:var(--magenta);flex:none"></span><div><div class="h-small" style="color:#fff">Heading</div><div class="p-white">Short note on this point.</div></div></div>
    <div style="display:flex;gap:7px;align-items:center"><span class="circle" style="width:22px;height:22px;background:var(--magenta);flex:none"></span><div><div class="h-small" style="color:#fff">Heading</div><div class="p-white">Short note on this point.</div></div></div>
    <div style="display:flex;gap:7px;align-items:center"><span class="circle" style="width:22px;height:22px;background:var(--magenta);flex:none"></span><div><div class="h-small" style="color:#fff">Heading</div><div class="p-white">Short note on this point.</div></div></div>
  </div>
  <div class="foot"><span class="dot"></span><span class="legal">© 2024 Corvane Semiconductor · corvane-semi.example</span><span class="sq"></span></div>
</section>

<section class="slide section" style="background:var(--green)">
  <div class="ring"></div>
  <span class="mark" style="left:140px;top:140px"></span>
  <div class="label" style="left:110px;top:178px">Section Break</div>
  <div class="sub" style="left:110px;top:198px">Short supporting text about this topic goes in this area.</div>
</section>

<section class="slide section" style="background:var(--purple)">
  <div class="ring"></div>
  <span class="mark" style="left:70px;top:146px"></span>
  <div class="label" style="left:40px;top:184px">Section Break</div>
  <div class="sub" style="left:40px;top:204px">Short supporting text about this topic goes in this area.</div>
</section>

<section class="slide">
  <h2 class="slide-title">Your Title Here</h2>
  <div class="ph" role="img" aria-label="Photo of a modern office atrium" style="left:0;top:80px;width:86px;height:110px;background:linear-gradient(180deg,#cfd9df,#8fa2ad)"></div>
  <div class="abs" style="left:86px;top:90px;width:180px;height:90px;background:var(--teal)"><span class="abs circle" style="left:76px;top:18px;width:28px;height:28px;border:2px solid #fff"></span><div class="p-white abs" style="left:20px;top:56px;width:140px;text-align:center">Short note on this point.</div></div>
  <div class="ph" role="img" aria-label="Photo of hands on a laptop keyboard" style="left:266px;top:80px;width:124px;height:110px;background:linear-gradient(180deg,#9aa6ae,#4e5a62)"></div>
  <div class="foot"><span class="dot"></span><span class="legal">© 2024 Corvane Semiconductor · corvane-semi.example</span><span class="sq"></span></div>
</section>

<section class="slide">
  <div class="ph" role="img" aria-label="Photo of two colleagues looking at a screen" style="inset:0 0 22px 0;background:linear-gradient(120deg,#b9c6cd,#6d7f8a 60%,#42515a)"></div>
  <div class="abs" style="right:0;top:70px;width:150px;height:110px;background:var(--teal);padding:12px">
    <div style="font-family:Raleway,Arial,sans-serif;font-size:13px;color:#fff;margin-bottom:6px">About Us</div>
    <div class="p-white">Short supporting text about this topic goes in this area. Short supporting text about this topic goes in this area.</div>
  </div>
  <div class="foot"><span class="dot"></span><span class="legal">© 2024 Corvane Semiconductor · corvane-semi.example</span><span class="sq"></span></div>
</section>

<section class="slide">
  <h2 class="slide-title">Your Title Goes Here</h2>
  <div class="abs p" style="left:14px;top:44px;width:120px">Short supporting text about this topic goes in this area.<br><br>Short supporting text about this topic goes in this area.<br><br>Short supporting text about this topic goes in this area.<br><br>Short supporting text about this topic goes in this area.</div>
  <div class="ph" role="img" aria-label="Desktop monitor showing a video of a smiling presenter" style="left:150px;top:60px;width:220px;height:130px;background:linear-gradient(135deg,#dfe6ea,#9fb0ba);border:5px solid #2a2a2a"></div>
  <div class="abs" style="left:238px;top:190px;width:44px;height:16px;background:#cfcfcf"></div>
  <div class="foot"><span class="dot"></span><span class="legal">© 2024 Corvane Semiconductor · corvane-semi.example</span><span class="sq"></span></div>
</section>

<section class="slide section" style="background:var(--teal)">
  <div class="ring"></div>
  <span class="circle abs" style="left:22px;top:128px;width:26px;height:26px;background:#fff"></span>
  <div class="label" style="left:20px;top:168px">Section Break</div>
  <div class="sub" style="left:20px;top:188px">Short supporting text about this topic goes in this area.</div>
</section>

<section class="slide">
  <h2 class="slide-title">Title And Image + Text</h2>
  <div class="ph" role="img" aria-label="Photo of people walking through a glass building" style="left:12px;top:34px;width:190px;height:64px;background:linear-gradient(90deg,#cbd5db,#8b9aa3)"></div>
  <div class="abs" style="left:202px;top:34px;width:176px;height:64px;background:var(--teal);padding:10px"><div class="p-white">Short supporting text about this topic goes in this area.</div></div>
  <div class="abs p" style="left:12px;top:110px;width:366px">Short supporting text about this topic goes in this area. Short supporting text about this topic goes in this area. Short supporting text about this topic goes in this area.<br><br>Short supporting text about this topic goes in this area. Short supporting text about this topic goes in this area.</div>
  <div class="foot"><span class="dot"></span><span class="legal">© 2024 Corvane Semiconductor · corvane-semi.example</span><span class="sq"></span></div>
</section>

<section class="slide">
  <h2 class="slide-title">About Us</h2>
  <div class="ph" role="img" aria-label="Photo of a man walking past tall office windows" style="left:12px;top:34px;width:120px;height:100px;background:linear-gradient(180deg,#e2e9ee,#a8b8c2)"></div>
  <div class="abs" style="left:214px;top:0;width:176px;height:140px;background:var(--sky);overflow:hidden"><span class="circle abs" style="right:-40px;top:40px;width:160px;height:160px;background:rgba(255,255,255,.15)"></span></div>
  <div class="abs p" style="left:12px;top:150px;width:366px">Short supporting text about this topic goes in this area. Short supporting text about this topic goes in this area. Short supporting text about this topic goes in this area.</div>
  <div class="foot"><span class="dot"></span><span class="legal">© 2024 Corvane Semiconductor · corvane-semi.example</span><span class="sq"></span></div>
</section>

<section class="slide">
  <h2 class="slide-title">Company Details</h2>
  <div class="abs p" style="left:16px;top:44px;width:190px">
    <b style="color:var(--ink)">Founded:</b> Short note on this point.<br><br>
    <b style="color:var(--ink)">Offices:</b> Short note on this point.<br><br>
    <b style="color:var(--ink)">Markets:</b> Short note on this point.<br><br>
    <b style="color:var(--ink)">People:</b> Short note on this point.
  </div>
  <div class="abs" style="left:244px;top:58px;width:120px;height:100px;background:var(--teal);display:flex;align-items:center;justify-content:center"><span class="brand brand-white" style="font-size:15px"><i style="width:11px;height:11px"></i>Corvane</span></div>
  <div class="foot"><span class="dot"></span><span class="legal">© 2024 Corvane Semiconductor · corvane-semi.example</span><span class="sq"></span></div>
</section>

<section class="slide" style="background:var(--teal)">
  <h2 class="slide-title" style="color:#fff">About Us</h2>
  <div class="ph circle" role="img" aria-label="Round portrait photo of a team member" style="left:172px;top:52px;width:46px;height:46px;background:linear-gradient(135deg,#f0d9c6,#9aa9b2);border:2px solid #fff"></div>
  <div class="abs p-white" style="left:60px;top:118px;width:270px;text-align:center">Short supporting text about this topic goes in this area. Short supporting text about this topic goes in this area.</div>
  <div class="abs" style="left:177px;top:160px;display:flex;gap:6px"><span class="circle" style="width:10px;height:10px;background:#fff"></span><span class="circle" style="width:10px;height:10px;background:#fff"></span><span class="circle" style="width:10px;height:10px;background:#fff"></span></div>
</section>

<section class="slide">
  <h2 class="slide-title">Your Blank Slide</h2>
  <div class="foot"><span class="dot"></span><span class="legal">© 2024 Corvane Semiconductor · corvane-semi.example</span><span class="sq"></span></div>
</section>

<section class="slide">
  <div class="abs" style="left:12px;top:14px;width:60px;height:22px;background:#2a2a2a"></div>
  <div class="abs" style="left:128px;top:14px;width:56px;height:22px;border:2px solid #2a2a2a"></div>
  <div class="abs" style="left:206px;top:16px;width:62px;height:18px;background:#2a2a2a"></div>
  <div class="abs" style="left:296px;top:8px;width:40px;height:40px;border-radius:50%;border:2px solid #2a2a2a"></div>
  <div class="abs" style="left:12px;top:96px;width:56px;height:24px;border:2px solid #2a2a2a"></div>
  <div class="abs" style="left:130px;top:82px;width:130px;height:66px;background:var(--cyan);display:flex;align-items:center;justify-content:center;text-align:center;font-family:Raleway,Arial,sans-serif;font-size:18px;line-height:1.1;color:#fff">Our<br>Portfolio</div>
  <div class="abs" style="left:306px;top:88px;width:42px;height:42px;border-radius:50%;border:2px solid #2a2a2a"></div>
  <div class="abs" style="left:12px;top:184px;width:60px;height:24px;background:#2a2a2a"></div>
  <div class="abs" style="left:120px;top:180px;width:70px;height:28px;background:#2a2a2a"></div>
  <div class="abs" style="left:210px;top:184px;width:40px;height:24px;border:2px solid #2a2a2a"></div>
  <div class="abs" style="left:290px;top:178px;width:70px;height:30px;border:2px solid #2a2a2a;border-radius:4px"></div>
  <div class="foot"><span class="dot"></span><span class="legal">© 2024 Corvane Semiconductor · corvane-semi.example</span><span class="sq"></span></div>
</section>

<section class="slide">
  <h2 class="slide-title">Three Bullets Area</h2>
  <div class="ph" role="img" aria-label="Photo of a desk with a laptop and papers" style="left:0;top:32px;width:390px;height:82px;background:linear-gradient(90deg,#dde3e7,#f3f5f6 50%,#b7c1c8)"></div>
  <div class="abs" style="left:0;top:114px;width:390px;display:flex;justify-content:space-around">
    <div style="width:100px;text-align:center"><span class="circle" style="display:block;margin:-14px auto 6px;width:28px;height:28px;background:var(--teal)"></span><div class="h-small">Heading</div><div class="p">Short note on this point.</div></div>
    <div style="width:100px;text-align:center"><span class="circle" style="display:block;margin:-14px auto 6px;width:28px;height:28px;background:var(--teal)"></span><div class="h-small">Heading</div><div class="p">Short note on this point.</div></div>
    <div style="width:100px;text-align:center"><span class="circle" style="display:block;margin:-14px auto 6px;width:28px;height:28px;background:var(--teal)"></span><div class="h-small">Heading</div><div class="p">Short note on this point.</div></div>
  </div>
  <div class="foot"><span class="dot"></span><span class="legal">© 2024 Corvane Semiconductor · corvane-semi.example</span><span class="sq"></span></div>
</section>

<section class="slide section" style="background:var(--magenta)">
  <div class="ring"></div>
  <span class="mark" style="left:50px;top:150px"></span>
  <div class="label" style="left:20px;top:188px">Section Break</div>
  <div class="sub" style="left:20px;top:208px">Short supporting text about this topic goes in this area.</div>
</section>

<section class="slide">
  <h2 class="slide-title">Four Column Area</h2>
  <div class="abs" style="left:14px;top:60px;right:14px;display:flex;gap:10px">
    <div style="flex:1;height:120px;border:1px solid var(--line);text-align:center;padding-top:10px"><span class="circle" style="display:block;margin:0 auto 8px;width:26px;height:26px;background:var(--teal)"></span><div class="h-small" style="color:var(--teal)">Heading</div><div class="p">Short note on this point.</div></div>
    <div style="flex:1;height:120px;border:1px solid var(--line);text-align:center;padding-top:10px"><span class="circle" style="display:block;margin:0 auto 8px;width:26px;height:26px;background:var(--magenta)"></span><div class="h-small" style="color:var(--magenta)">Heading</div><div class="p">Short note on this point.</div></div>
    <div style="flex:1;height:120px;border:1px solid var(--line);text-align:center;padding-top:10px"><span class="circle" style="display:block;margin:0 auto 8px;width:26px;height:26px;background:var(--green)"></span><div class="h-small" style="color:var(--green)">Heading</div><div class="p">Short note on this point.</div></div>
    <div style="flex:1;height:120px;border:1px solid var(--line);text-align:center;padding-top:10px"><span class="circle" style="display:block;margin:0 auto 8px;width:26px;height:26px;background:var(--orange)"></span><div class="h-small" style="color:var(--orange)">Heading</div><div class="p">Short note on this point.</div></div>
  </div>
  <div class="foot"><span class="dot"></span><span class="legal">© 2024 Corvane Semiconductor · corvane-semi.example</span><span class="sq"></span></div>
</section>

<section class="slide">
  <h2 class="slide-title">Circle Infographic</h2>
  <svg class="abs" style="left:135px;top:48px" width="120" height="120" viewBox="0 0 120 120">
    <g transform="rotate(-90 60 60)" fill="none" stroke-width="20">
      <circle cx="60" cy="60" r="44" stroke="var(--teal)" stroke-dasharray="43 234" stroke-dashoffset="0"/>
      <circle cx="60" cy="60" r="44" stroke="var(--green)" stroke-dasharray="43 234" stroke-dashoffset="-46"/>
      <circle cx="60" cy="60" r="44" stroke="var(--orange)" stroke-dasharray="43 234" stroke-dashoffset="-92"/>
      <circle cx="60" cy="60" r="44" stroke="var(--magenta)" stroke-dasharray="43 234" stroke-dashoffset="-138"/>
      <circle cx="60" cy="60" r="44" stroke="var(--purple)" stroke-dasharray="43 234" stroke-dashoffset="-184"/>
      <circle cx="60" cy="60" r="44" stroke="var(--cyan)" stroke-dasharray="43 234" stroke-dashoffset="-230"/>
    </g>
    <circle cx="60" cy="60" r="20" fill="var(--teal)"/>
  </svg>
  <div class="abs" style="left:30px;top:62px;text-align:right;width:96px"><div class="h-small" style="color:var(--cyan)">Heading</div><div class="p">Short note here.</div></div>
  <div class="abs" style="left:30px;top:110px;text-align:right;width:96px"><div class="h-small" style="color:var(--purple)">Heading</div><div class="p">Short note here.</div></div>
  <div class="abs" style="left:30px;top:150px;text-align:right;width:96px"><div class="h-small" style="color:var(--magenta)">Heading</div><div class="p">Short note here.</div></div>
  <div class="abs" style="left:266px;top:62px;width:96px"><div class="h-small">Heading</div><div class="p">Short note here.</div></div>
  <div class="abs" style="left:266px;top:110px;width:96px"><div class="h-small" style="color:var(--green)">Heading</div><div class="p">Short note here.</div></div>
  <div class="abs" style="left:266px;top:150px;width:96px"><div class="h-small" style="color:var(--orange)">Heading</div><div class="p">Short note here.</div></div>
  <div class="foot"><span class="dot"></span><span class="legal">© 2024 Corvane Semiconductor · corvane-semi.example</span><span class="sq"></span></div>
</section>

<section class="slide">
  <h2 class="slide-title">Data Analysis</h2>
  <div class="abs p" style="left:14px;top:40px;width:150px">Short supporting text about this topic goes in this area. Short supporting text about this topic goes in this area.<br><br>Short supporting text about this topic goes in this area.</div>
  <div class="abs" style="left:14px;top:150px;width:130px;height:3px;background:var(--green)"></div>
  <div class="abs" style="left:14px;top:164px;width:130px;height:3px;background:var(--magenta)"></div>
  <div class="ph" role="img" aria-label="Photo of a woman at a window, tinted blue" style="left:176px;top:0;width:214px;height:258px;background:linear-gradient(160deg,#c6e7f1,#4fb3cf)"></div>
  <div class="abs circle" style="left:210px;top:48px;width:64px;height:64px;border:2px solid #fff;display:flex;align-items:center;justify-content:center;color:#fff"><span class="num" style="font-size:18px">750</span></div>
  <div class="abs circle" style="left:296px;top:104px;width:64px;height:64px;border:2px solid #fff;display:flex;align-items:center;justify-content:center;color:#fff"><span class="num" style="font-size:18px">50%</span></div>
  <div class="abs circle" style="left:210px;top:150px;width:64px;height:64px;border:2px solid #fff;display:flex;align-items:center;justify-content:center;color:#fff"><span class="num" style="font-size:18px">150</span></div>
  <div class="foot"><span class="dot"></span><span class="legal"></span></div>
</section>

<section class="slide section" style="background:var(--teal)">
  <div class="ring"></div>
  <span class="mark" style="left:44px;top:120px"></span>
  <div class="label" style="left:16px;top:156px">Section Break</div>
  <div class="sub" style="left:16px;top:176px">Short supporting text about this topic goes in this area.</div>
</section>

<section class="slide">
  <h2 class="slide-title">Global Experience</h2>
  <div class="ph" role="img" aria-label="Grey world map showing office locations" style="left:30px;top:38px;width:330px;height:160px;background:radial-gradient(ellipse at 50% 50%,#d6d6d6 0%,#e8e8e8 55%,#fff 75%)"></div>
  <span class="abs circle" style="left:110px;top:90px;width:8px;height:8px;background:var(--teal)"></span>
  <span class="abs circle" style="left:196px;top:84px;width:8px;height:8px;background:var(--teal)"></span>
  <span class="abs circle" style="left:214px;top:104px;width:8px;height:8px;background:var(--teal)"></span>
  <span class="abs circle" style="left:272px;top:96px;width:8px;height:8px;background:var(--teal)"></span>
  <span class="abs circle" style="left:300px;top:116px;width:8px;height:8px;background:var(--teal)"></span>
  <span class="abs circle" style="left:318px;top:150px;width:8px;height:8px;background:var(--teal)"></span>
  <div class="abs" style="left:30px;top:210px;display:flex;align-items:center;gap:5px"><span class="circle" style="width:8px;height:8px;background:var(--teal)"></span><span class="p">Office Locations</span></div>
  <div class="foot"><span class="dot"></span><span class="legal">© 2024 Corvane Semiconductor · corvane-semi.example</span><span class="sq"></span></div>
</section>

<section class="slide">
  <h2 class="slide-title">Portfolio Area</h2>
  <div class="ph" role="img" aria-label="Photo of people at a sunlit table" style="left:12px;top:36px;width:116px;height:78px;background:linear-gradient(135deg,#e0a66a,#7a5a3d)"></div>
  <div class="abs" style="left:128px;top:36px;width:116px;height:78px;background:var(--magenta);padding:8px"><div class="h-small" style="color:#fff">Heading Goes Here</div><div class="p-white">Short note on this point.</div></div>
  <div class="ph" role="img" aria-label="Photo of a sunset over a field" style="left:244px;top:36px;width:134px;height:78px;background:linear-gradient(135deg,#f6cf7a,#b77a3a)"></div>
  <div class="abs" style="left:12px;top:114px;width:116px;height:78px;background:var(--cyan);padding:8px"><div class="h-small" style="color:#fff">Heading Goes Here</div><div class="p-white">Short note on this point.</div></div>
  <div class="ph" role="img" aria-label="Photo of two people walking outdoors" style="left:128px;top:114px;width:116px;height:78px;background:linear-gradient(135deg,#b7c7a0,#5e7552)"></div>
  <div class="abs" style="left:244px;top:114px;width:134px;height:78px;background:var(--green);padding:8px"><div class="h-small" style="color:#fff">Heading Goes Here</div><div class="p-white">Short note on this point.</div></div>
  <div class="foot"><span class="dot"></span><span class="legal">© 2024 Corvane Semiconductor · corvane-semi.example</span><span class="sq"></span></div>
</section>

<section class="slide">
  <h2 class="slide-title">Our Team</h2>
  <div class="ph circle" role="img" aria-label="Round portrait photo of a team member" style="left:40px;top:60px;width:80px;height:80px;background:linear-gradient(135deg,#ecd3bf,#8b9ba5)"></div>
  <div class="abs" style="left:40px;top:148px;width:80px;text-align:center"><div class="h-small">Name Here</div><div class="p">Job Title</div></div>
  <div class="abs" style="left:66px;top:174px;display:flex;gap:4px"><span class="circle" style="width:8px;height:8px;background:var(--teal)"></span><span class="circle" style="width:8px;height:8px;background:var(--teal)"></span><span class="circle" style="width:8px;height:8px;background:var(--teal)"></span></div>
  <div class="abs p" style="left:150px;top:64px;width:220px">Short supporting text about this topic goes in this area. Short supporting text about this topic goes in this area.<br><br>Short supporting text about this topic goes in this area.</div>
  <div class="foot"><span class="dot"></span><span class="legal">© 2024 Corvane Semiconductor · corvane-semi.example</span><span class="sq"></span></div>
</section>

<section class="slide">
  <h2 class="slide-title">Chart Title</h2>
  <div class="abs" style="left:14px;right:14px;top:48px;display:flex;justify-content:space-between">
    <div style="width:80px;text-align:center">
      <svg width="46" height="46" viewBox="0 0 46 46"><circle cx="23" cy="23" r="19" fill="none" stroke="#e6e6e6" stroke-width="4"/><circle cx="23" cy="23" r="19" fill="none" stroke="var(--teal)" stroke-width="4" stroke-dasharray="90 120" transform="rotate(-90 23 23)"/><text x="23" y="26" text-anchor="middle" font-size="8" fill="var(--teal)" font-family="Open Sans,Arial,sans-serif">75%</text></svg>
      <div class="num" style="font-size:14px;color:var(--teal)">35,250</div><div class="p">Short note on this point.</div>
    </div>
    <div style="width:80px;text-align:center">
      <svg width="46" height="46" viewBox="0 0 46 46"><circle cx="23" cy="23" r="19" fill="none" stroke="#e6e6e6" stroke-width="4"/><circle cx="23" cy="23" r="19" fill="none" stroke="var(--magenta)" stroke-width="4" stroke-dasharray="72 120" transform="rotate(-90 23 23)"/><text x="23" y="26" text-anchor="middle" font-size="8" fill="var(--magenta)" font-family="Open Sans,Arial,sans-serif">60%</text></svg>
      <div class="num" style="font-size:14px;color:var(--magenta)">126,890</div><div class="p">Short note on this point.</div>
    </div>
    <div style="width:80px;text-align:center">
      <svg width="46" height="46" viewBox="0 0 46 46"><circle cx="23" cy="23" r="19" fill="none" stroke="#e6e6e6" stroke-width="4"/><circle cx="23" cy="23" r="19" fill="none" stroke="var(--green)" stroke-width="4" stroke-dasharray="54 120" transform="rotate(-90 23 23)"/><text x="23" y="26" text-anchor="middle" font-size="8" fill="var(--green)" font-family="Open Sans,Arial,sans-serif">45%</text></svg>
      <div class="num" style="font-size:14px;color:var(--green)">3,256</div><div class="p">Short note on this point.</div>
    </div>
    <div style="width:80px;text-align:center">
      <svg width="46" height="46" viewBox="0 0 46 46"><circle cx="23" cy="23" r="19" fill="none" stroke="#e6e6e6" stroke-width="4"/><circle cx="23" cy="23" r="19" fill="none" stroke="var(--orange)" stroke-width="4" stroke-dasharray="100 120" transform="rotate(-90 23 23)"/><text x="23" y="26" text-anchor="middle" font-size="8" fill="var(--orange)" font-family="Open Sans,Arial,sans-serif">85%</text></svg>
      <div class="num" style="font-size:14px;color:var(--orange)">11,456</div><div class="p">Short note on this point.</div>
    </div>
  </div>
  <div class="foot"><span class="dot"></span><span class="legal">© 2024 Corvane Semiconductor · corvane-semi.example</span><span class="sq"></span></div>
</section>

<section class="slide">
  <h2 class="slide-title">Price Slide</h2>
  <div class="abs" style="left:14px;right:14px;top:38px;display:flex;gap:6px">
    <div style="flex:1;border:1px solid var(--line);text-align:center"><div style="background:var(--teal);color:#fff;font-size:6px;padding:4px">Basic</div><div class="num" style="font-size:15px;padding:8px 0;color:var(--ink)">$99</div><div class="p" style="border-top:1px solid var(--line);padding:4px">Feature one<br>Feature two<br>Feature three<br>Feature four</div><div style="margin:6px auto 8px;width:40px;height:10px;background:var(--teal)"></div></div>
    <div style="flex:1;border:1px solid var(--line);text-align:center"><div style="background:var(--orange);color:#fff;font-size:6px;padding:4px">Standard</div><div class="num" style="font-size:15px;padding:8px 0;color:var(--ink)">$199</div><div class="p" style="border-top:1px solid var(--line);padding:4px">Feature one<br>Feature two<br>Feature three<br>Feature four</div><div style="margin:6px auto 8px;width:40px;height:10px;background:var(--orange)"></div></div>
    <div style="flex:1;border:1px solid var(--line);text-align:center"><div style="background:var(--magenta);color:#fff;font-size:6px;padding:4px">Plus</div><div class="num" style="font-size:15px;padding:8px 0;color:var(--ink)">$299</div><div class="p" style="border-top:1px solid var(--line);padding:4px">Feature one<br>Feature two<br>Feature three<br>Feature four</div><div style="margin:6px auto 8px;width:40px;height:10px;background:var(--magenta)"></div></div>
    <div style="flex:1;border:1px solid var(--line);text-align:center"><div style="background:var(--purple);color:#fff;font-size:6px;padding:4px">Pro</div><div class="num" style="font-size:15px;padding:8px 0;color:var(--ink)">$499</div><div class="p" style="border-top:1px solid var(--line);padding:4px">Feature one<br>Feature two<br>Feature three<br>Feature four</div><div style="margin:6px auto 8px;width:40px;height:10px;background:var(--purple)"></div></div>
    <div style="flex:1;border:1px solid var(--line);text-align:center"><div style="background:var(--cyan);color:#fff;font-size:6px;padding:4px">Premium</div><div class="num" style="font-size:15px;padding:8px 0;color:var(--ink)">$999</div><div class="p" style="border-top:1px solid var(--line);padding:4px">Feature one<br>Feature two<br>Feature three<br>Feature four</div><div style="margin:6px auto 8px;width:40px;height:10px;background:var(--cyan)"></div></div>
  </div>
  <div class="foot"><span class="dot"></span><span class="legal">© 2024 Corvane Semiconductor · corvane-semi.example</span><span class="sq"></span></div>
</section>

<section class="slide">
  <h2 class="slide-title">Pricing Table Plan</h2>
  <div class="abs" style="left:14px;right:14px;top:48px;display:flex;justify-content:space-between">
    <div style="width:62px;text-align:center"><span class="circle" style="display:block;margin:0 auto 5px;width:24px;height:24px;background:var(--green)"></span><div class="num" style="font-size:13px;color:var(--green)">$10</div><div class="p">Plan one<br>Feature one<br>Feature two<br>Feature three</div></div>
    <div style="width:62px;text-align:center"><span class="circle" style="display:block;margin:0 auto 5px;width:24px;height:24px;background:var(--orange)"></span><div class="num" style="font-size:13px;color:var(--orange)">$20</div><div class="p">Plan two<br>Feature one<br>Feature two<br>Feature three</div></div>
    <div style="width:62px;text-align:center"><span class="circle" style="display:block;margin:0 auto 5px;width:24px;height:24px;background:var(--purple)"></span><div class="num" style="font-size:13px;color:var(--purple)">$30</div><div class="p">Plan three<br>Feature one<br>Feature two<br>Feature three</div></div>
    <div style="width:62px;text-align:center"><span class="circle" style="display:block;margin:0 auto 5px;width:24px;height:24px;background:var(--magenta)"></span><div class="num" style="font-size:13px;color:var(--magenta)">$40</div><div class="p">Plan four<br>Feature one<br>Feature two<br>Feature three</div></div>
    <div style="width:62px;text-align:center"><span class="circle" style="display:block;margin:0 auto 5px;width:24px;height:24px;background:var(--cyan)"></span><div class="num" style="font-size:13px;color:var(--cyan)">$50</div><div class="p">Plan five<br>Feature one<br>Feature two<br>Feature three</div></div>
  </div>
  <div class="foot"><span class="dot"></span><span class="legal">© 2024 Corvane Semiconductor · corvane-semi.example</span><span class="sq"></span></div>
</section>

<section class="slide">
  <h2 class="slide-title">Social Media Marketing</h2>
  <div class="abs" style="left:40px;right:40px;top:40px;height:200px;display:flex;justify-content:space-between;align-items:flex-end">
    <div style="width:44px;height:100%;position:relative;background:#f0f0f0"><span class="circle abs" style="left:8px;top:0;width:28px;height:28px;background:var(--teal)"></span><div class="abs" style="left:8px;right:8px;bottom:0;height:60%;background:var(--cyan);display:flex;align-items:flex-start;justify-content:center;color:#fff;font-size:7px;padding-top:4px">62</div></div>
    <div style="width:44px;height:100%;position:relative;background:#f0f0f0"><span class="circle abs" style="left:8px;top:0;width:28px;height:28px;background:var(--teal)"></span><div class="abs" style="left:8px;right:8px;bottom:0;height:42%;background:var(--magenta);display:flex;align-items:flex-start;justify-content:center;color:#fff;font-size:7px;padding-top:4px">54</div></div>
    <div style="width:44px;height:100%;position:relative;background:#f0f0f0"><span class="circle abs" style="left:8px;top:0;width:28px;height:28px;background:var(--teal)"></span><div class="abs" style="left:8px;right:8px;bottom:0;height:55%;background:var(--green);display:flex;align-items:flex-start;justify-content:center;color:#fff;font-size:7px;padding-top:4px">76</div></div>
    <div style="width:44px;height:100%;position:relative;background:#f0f0f0"><span class="circle abs" style="left:8px;top:0;width:28px;height:28px;background:var(--teal)"></span><div class="abs" style="left:8px;right:8px;bottom:0;height:22%;background:var(--orange);display:flex;align-items:flex-start;justify-content:center;color:#fff;font-size:7px;padding-top:4px">17</div></div>
  </div>
</section>

<section class="slide">
  <h2 class="slide-title">3D Pie Chart</h2>
  <div class="abs" style="left:44px;top:46px;font-size:7px;color:var(--ink)">Sales Report</div>
  <svg class="abs" style="left:24px;top:60px" width="130" height="130" viewBox="0 0 130 130">
    <g transform="rotate(-90 65 65)" fill="none" stroke-width="56">
      <circle cx="65" cy="65" r="28" stroke="var(--cyan)" stroke-dasharray="62 176"/>
      <circle cx="65" cy="65" r="28" stroke="var(--teal)" stroke-dasharray="48 176" stroke-dashoffset="-62"/>
      <circle cx="65" cy="65" r="28" stroke="var(--green)" stroke-dasharray="24 176" stroke-dashoffset="-110"/>
      <circle cx="65" cy="65" r="28" stroke="var(--magenta)" stroke-dasharray="26 176" stroke-dashoffset="-134"/>
      <circle cx="65" cy="65" r="28" stroke="var(--purple)" stroke-dasharray="16 176" stroke-dashoffset="-160"/>
    </g>
  </svg>
  <div class="abs" style="left:200px;top:70px;display:flex;flex-direction:column;gap:9px">
    <div style="display:flex;gap:5px;align-items:center"><span style="width:8px;height:8px;background:var(--cyan)"></span><span class="p">Product line one</span></div>
    <div style="display:flex;gap:5px;align-items:center"><span style="width:8px;height:8px;background:var(--teal)"></span><span class="p">Product line two</span></div>
    <div style="display:flex;gap:5px;align-items:center"><span style="width:8px;height:8px;background:var(--green)"></span><span class="p">Product line three</span></div>
    <div style="display:flex;gap:5px;align-items:center"><span style="width:8px;height:8px;background:var(--magenta)"></span><span class="p">Product line four</span></div>
    <div style="display:flex;gap:5px;align-items:center"><span style="width:8px;height:8px;background:var(--purple)"></span><span class="p">Product line five</span></div>
  </div>
  <div class="foot"><span class="dot"></span><span class="legal">© 2024 Corvane Semiconductor · corvane-semi.example</span><span class="sq"></span></div>
</section>

<section class="slide">
  <h2 class="slide-title">Bar Chart</h2>
  <svg class="abs" style="left:20px;top:40px" width="350" height="150" viewBox="0 0 350 150">
    <g stroke="#eee"><line x1="0" y1="20" x2="350" y2="20"/><line x1="0" y1="60" x2="350" y2="60"/><line x1="0" y1="100" x2="350" y2="100"/><line x1="0" y1="140" x2="350" y2="140"/></g>
    <g>
      <rect x="20" y="70" width="10" height="70" fill="var(--magenta)"/><rect x="31" y="50" width="10" height="90" fill="var(--cyan)"/><rect x="42" y="90" width="10" height="50" fill="var(--green)"/><rect x="53" y="80" width="10" height="60" fill="var(--orange)"/>
      <rect x="100" y="40" width="10" height="100" fill="var(--magenta)"/><rect x="111" y="80" width="10" height="60" fill="var(--cyan)"/><rect x="122" y="60" width="10" height="80" fill="var(--green)"/><rect x="133" y="96" width="10" height="44" fill="var(--orange)"/>
      <rect x="180" y="86" width="10" height="54" fill="var(--magenta)"/><rect x="191" y="30" width="10" height="110" fill="var(--cyan)"/><rect x="202" y="76" width="10" height="64" fill="var(--green)"/><rect x="213" y="56" width="10" height="84" fill="var(--orange)"/>
      <rect x="260" y="60" width="10" height="80" fill="var(--magenta)"/><rect x="271" y="92" width="10" height="48" fill="var(--cyan)"/><rect x="282" y="44" width="10" height="96" fill="var(--green)"/><rect x="293" y="70" width="10" height="70" fill="var(--orange)"/>
    </g>
  </svg>
  <div class="abs p" style="left:20px;top:200px;width:350px">Short supporting text about this topic goes in this area. Short supporting text about this topic goes in this area.</div>
  <div class="foot"><span class="dot"></span><span class="legal">© 2024 Corvane Semiconductor · corvane-semi.example</span><span class="sq"></span></div>
</section>

<section class="slide">
  <h2 class="slide-title">Financial Slides</h2>
  <svg class="abs" style="left:18px;top:70px" width="160" height="110" viewBox="0 0 160 110">
    <g stroke="#eee"><line x1="0" y1="10" x2="160" y2="10"/><line x1="0" y1="55" x2="160" y2="55"/><line x1="0" y1="100" x2="160" y2="100"/></g>
    <polyline points="5,80 45,30 85,70 125,20 155,60" fill="none" stroke="var(--magenta)" stroke-width="2"/>
    <polyline points="5,60 45,70 85,40 125,76 155,40" fill="none" stroke="var(--cyan)" stroke-width="2"/>
  </svg>
  <div class="abs" style="left:204px;top:44px;width:170px"><div class="h-small" style="color:var(--magenta)">Heading Goes Here</div><div class="p">Short note on this point.</div></div>
  <svg class="abs" style="left:204px;top:90px" width="170" height="110" viewBox="0 0 170 110">
    <g><rect x="5" y="40" width="12" height="70" fill="var(--magenta)"/><rect x="19" y="20" width="12" height="90" fill="var(--cyan)"/>
    <rect x="50" y="60" width="12" height="50" fill="var(--magenta)"/><rect x="64" y="30" width="12" height="80" fill="var(--cyan)"/>
    <rect x="95" y="10" width="12" height="100" fill="var(--magenta)"/><rect x="109" y="50" width="12" height="60" fill="var(--cyan)"/>
    <rect x="140" y="36" width="12" height="74" fill="var(--magenta)"/><rect x="154" y="64" width="12" height="46" fill="var(--cyan)"/></g>
  </svg>
  <div class="foot"><span class="dot"></span><span class="legal">© 2024 Corvane Semiconductor · corvane-semi.example</span><span class="sq"></span></div>
</section>

<section class="slide">
  <h2 class="slide-title">Table Slide</h2>
  <div class="abs" style="left:14px;right:14px;top:42px">
    <table class="table">
      <tr><th>Item</th><th>Q1</th><th>Q2</th><th>Q3</th><th>Q4</th><th>Total</th></tr>
      <tr><td>Item one</td><td>120</td><td>140</td><td>160</td><td>180</td><td>600</td></tr>
      <tr><td>Item two</td><td>90</td><td>110</td><td>130</td><td>150</td><td>480</td></tr>
      <tr><td>Item three</td><td>60</td><td>80</td><td>70</td><td>90</td><td>300</td></tr>
      <tr><td>Item four</td><td>140</td><td>120</td><td>150</td><td>170</td><td>580</td></tr>
      <tr><td>Item five</td><td>75</td><td>95</td><td>85</td><td>105</td><td>360</td></tr>
      <tr><td>Item six</td><td>50</td><td>65</td><td>70</td><td>80</td><td>265</td></tr>
    </table>
  </div>
  <div class="foot"><span class="dot"></span><span class="legal">© 2024 Corvane Semiconductor · corvane-semi.example</span><span class="sq"></span></div>
</section>

<section class="slide">
  <h2 class="slide-title">Our Team</h2>
  <div class="abs" style="left:20px;top:44px;width:360px;display:grid;grid-template-columns:1fr 1fr;row-gap:30px">
    <div style="display:flex;gap:8px"><span class="ph circle" role="img" aria-label="Round portrait photo of a team member" style="position:static;flex:none;width:34px;height:34px;background:linear-gradient(135deg,#ecd3bf,#8b9ba5)"></span><div><div class="h-small">Name Here</div><div class="p">Job Title<br>Short note on this point.</div></div></div>
    <div style="display:flex;gap:8px"><span class="ph circle" role="img" aria-label="Round portrait photo of a team member" style="position:static;flex:none;width:34px;height:34px;background:linear-gradient(135deg,#ecd3bf,#8b9ba5)"></span><div><div class="h-small">Name Here</div><div class="p">Job Title<br>Short note on this point.</div></div></div>
    <div style="display:flex;gap:8px"><span class="ph circle" role="img" aria-label="Round portrait photo of a team member" style="position:static;flex:none;width:34px;height:34px;background:linear-gradient(135deg,#ecd3bf,#8b9ba5)"></span><div><div class="h-small">Name Here</div><div class="p">Job Title<br>Short note on this point.</div></div></div>
    <div style="display:flex;gap:8px"><span class="ph circle" role="img" aria-label="Round portrait photo of a team member" style="position:static;flex:none;width:34px;height:34px;background:linear-gradient(135deg,#ecd3bf,#8b9ba5)"></span><div><div class="h-small">Name Here</div><div class="p">Job Title<br>Short note on this point.</div></div></div>
  </div>
  <div class="foot"><span class="dot"></span><span class="legal">© 2024 Corvane Semiconductor · corvane-semi.example</span><span class="sq"></span></div>
</section>

<section class="slide">
  <div class="ph" role="img" aria-label="Photo of a woman running outdoors with a wearable device, tinted teal" style="inset:0;background:linear-gradient(135deg,#7fd0e0,#2aa3bd 55%,#15809b)"></div>
  <div class="abs" style="left:16px;top:110px;color:#fff">
    <div style="font-family:Raleway,Arial,sans-serif;font-weight:600;font-size:20px;line-height:1.2">Shaping a Smarter<br>Wired World</div>
    <div style="font-size:7px;margin-top:6px">www.corvane-semi.example</div>
  </div>
  <div class="abs p-white" style="right:16px;bottom:14px;width:60px;text-align:right">Short closing note here.</div>
</section>

</main>
</body>
</html>
```